i need a template design for online store

hi great designers, i need a template for any online store. But preferably well owned shopping carts. I would be an added advantage if the store is setup for me. I need a mature and attractive colours. My online store deals in electronics.

Shopping

1 page

```html
<!DOCTYPE html>
<html lang="en">
<head>
<meta charset="utf-8">
<title>Circuit Cove — Online Shop Template</title>
<link rel="stylesheet" href="https://fonts.googleapis.com/css2?family=Josefin+Sans:wght@300;400;600;700&display=swap">
<style>
  :root {
    --navy: #1f3a78;
    --navy-deep: #0f2a66;
    --ink: #333333;
    --muted: #6a6a6a;
    --price-red: #b0283a;
    --bar-grey: #e2e2e2;
    --cat-grey: #cdcdcd;
    --footer-grey: #dedede;
    --base-grey: #7b7b7b;
    --white: #ffffff;
    --hero-light: #e9ecef;
    --hero-mid: #c9cdd2;
    --phone-dark: #2a2c31;
    --phone-mid: #6b6e74;
  }
  * { box-sizing: border-box; margin: 0; padding: 0; }
  html, body { width: 1200px; height: 2500px; overflow: hidden; background: var(--white); }
  body { position: relative; font-family: "Josefin Sans", sans-serif; color: var(--ink); }

  /* Hero */
  .hero { position: absolute; left: 0; top: 0; width: 1200px; height: 567px; }
  .hero-photo { position: absolute; inset: 0;
    background: linear-gradient(100deg, var(--hero-mid) 0%, var(--hero-light) 35%, #f2f2f0 60%, #d9c9bd 85%, #b9a293 100%); }
  .hero-panel { position: absolute; left: 208px; top: 202px; width: 782px; height: 225px;
    border: 2px solid rgba(255,255,255,.9); background: rgba(255,255,255,.38); text-align: center; }
  .hero-title { margin-top: 38px; font-size: 50px; font-weight: 400; letter-spacing: 3px; color: #6b6b6b; }
  .hero-rule { width: 330px; height: 1px; background: #9a9a9a; margin: 14px auto 16px; }
  .hero-sub { font-size: 27px; font-weight: 400; line-height: 42px; letter-spacing: 2px; color: #707070; }
  .hero-button { position: absolute; left: 521px; top: 440px; width: 156px; height: 45px;
    background: var(--navy-deep); color: var(--white); font-size: 19px; letter-spacing: 1px;
    display: flex; align-items: center; justify-content: center; padding-top: 3px; }

  /* Header bar */
  .header-bar { position: absolute; left: 0; top: 567px; width: 1200px; height: 85px; background: var(--bar-grey); }
  .brand { position: absolute; left: 90px; top: 31px; color: var(--navy); font-size: 26px; font-weight: 600;
    letter-spacing: 1px; line-height: 1; white-space: nowrap; }
  .main-nav a { position: absolute; top: 39px; font-size: 11px; letter-spacing: .5px; color: #555; text-decoration: none; white-space: nowrap; }
  .cart { position: absolute; left: 879px; top: 6px; width: 321px; height: 75px; }
  .cart-label { position: absolute; left: 111px; top: 12px; color: var(--white); font-size: 27px; letter-spacing: 1px; }
  .cart-count { position: absolute; left: 111px; top: 43px; color: var(--white); font-size: 17px; letter-spacing: 1px; }
  .cart-count b { color: #f0a43a; font-weight: 600; }

  .category-bar { position: absolute; left: 0; top: 652px; width: 1200px; height: 25px; background: var(--cat-grey); }
  .category-bar span { position: absolute; top: 8px; font-size: 9.5px; letter-spacing: .3px; color: #5a5a5a; white-space: nowrap; }
  .search { position: absolute; left: 787px; top: 3px; width: 240px; height: 19px; background: var(--white);
    border: 1px solid #bbb; font-size: 10px; color: #888; padding: 4px 6px; letter-spacing: .5px; }

  /* What's new */
  .section-title { position: absolute; left: 0; width: 1200px; text-align: center; top: 724px;
    font-size: 21px; font-weight: 600; letter-spacing: 2px; color: var(--navy); }
  .product { position: absolute; width: 180px; }
  .product-photo { width: 136px; height: 130px; margin-left: 22px;
    background: linear-gradient(90deg, var(--phone-dark) 0%, var(--phone-dark) 52%, var(--phone-mid) 58%, #9a9ca1 100%);
    border-radius: 10px; }
  .product-name { margin-top: 24px; font-size: 16px; font-weight: 600; letter-spacing: 1px; color: var(--navy); line-height: 18px; }
  .product-desc { margin-top: 5px; font-size: 9.6px; line-height: 12px; color: #666; text-align: justify; height: 72px; overflow: hidden; }
  .product-price { margin-top: 8px; white-space: nowrap; line-height: 28px; }
  .old { font-size: 16px; color: #777; text-decoration: line-through; margin-right: 6px; }
  .now { font-size: 25px; color: var(--price-red); }
  .see-more { position: absolute; left: 883px; top: 1756px; font-size: 18px; font-weight: 600; letter-spacing: 1px; color: var(--navy); }
  .see-more i { font-style: normal; color: #999; font-size: 13px; }

  /* Summer sale */
  .promo { position: absolute; top: 1819px; width: 250px; text-align: center; }
  .promo-photo { width: 250px; height: 191px;
    background: linear-gradient(120deg, #e4e8ec 0%, #c8ccd1 40%, #d7c1b3 75%, #a98d7e 100%); }
  .promo-title { margin-top: 22px; font-size: 24px; font-weight: 600; letter-spacing: 1px; color: var(--navy); line-height: 26px; }
  .promo-text { margin-top: 6px; font-size: 13px; line-height: 15px; color: #444; text-align: justify; }

  /* Footer */
  .site-footer { position: absolute; left: 0; top: 2208px; width: 1200px; height: 250px; background: var(--footer-grey); }
  .site-footer .f { position: absolute; font-size: 11px; letter-spacing: 1px; color: #777; }
  .site-footer .h { position: absolute; font-size: 15px; font-weight: 600; letter-spacing: 1px; color: var(--navy); }
  .footer-divider { position: absolute; left: 867px; top: 33px; width: 1px; height: 184px; background: #b5b5b5; }
  .social-dot { position: absolute; width: 20px; height: 20px; border-radius: 50%; background: #1a1a1a; }
  .base-bar { position: absolute; left: 0; top: 2458px; width: 1200px; height: 42px; background: var(--base-grey);
    color: var(--white); font-size: 16px; text-align: center; padding-top: 14px; letter-spacing: .5px; }
</style>
</head>
<body>

<header class="hero">
  <div class="hero-photo" role="img" aria-label="Photo of hands holding smartphones in a bright room"></div>
  <div class="hero-panel">
    <h1 class="hero-title">30% OFF THIS SUMMER</h1>
    <div class="hero-rule"></div>
    <p class="hero-sub">ALL SMARTPHONES IN OUR STORE<br>WITH UNBELIEVABLE PRICES</p>
  </div>
  <a class="hero-button">SEE MORE</a>
</header>

<div class="header-bar">
  <div class="brand">CIRCUIT COVE</div>
  <nav class="main-nav">
    <a style="left:327px">ABOUT US</a>
    <a style="left:425px">NEWS</a>
    <a style="left:500px">SERVICES</a>
    <a style="left:577px">TODAY DEALS</a>
    <a style="left:690px">HELP</a>
    <a style="left:773px">SIGN IN</a>
  </nav>
  <div class="cart">
    <svg width="321" height="75" viewBox="0 0 321 75" style="position:absolute;left:0;top:0">
      <polygon points="32,0 321,0 321,75 32,75 0,37.5" fill="var(--navy-deep)"/>
      <g fill="none" stroke="#fff" stroke-width="3.5" stroke-linejoin="round" stroke-linecap="round">
        <path d="M44 22 H54 L62 50 H90 L96 30 H57"/>
      </g>
      <circle cx="66" cy="58" r="4" fill="#fff"/>
      <circle cx="86" cy="58" r="4" fill="#fff"/>
    </svg>
    <div class="cart-label">CART</div>
    <div class="cart-count"><b>0</b> PRODUCTS</div>
  </div>
</div>

<div class="category-bar">
  <span style="left:171px">CELL PHONES</span>
  <span style="left:273px">COMPUTERS</span>
  <span style="left:365px">TV/VIDEO</span>
  <span style="left:433px">AUDIO</span>
  <span style="left:490px">CAMERAS</span>
  <span style="left:565px">CAR</span>
  <span style="left:606px">OFFICE</span>
  <span style="left:669px">MUSIC</span>
  <span style="left:725px">OTHERS</span>
  <div class="search">SEARCH</div>
</div>

<main>
  <h2 class="section-title">WHAT'S NEW</h2>

  <!-- Row 1 -->
  <article class="product" style="left:208px;top:790px"><div class="product-photo" role="img" aria-label="Smartphone product photo"></div><h3 class="product-name">LOREM IPSUM</h3><p class="product-desc">Lorem ipsum dolor sit amet, consectetur adipiscing elit. Nulla congue risus ut nisl placerat, sed rutrum lacus dignissim. Donec fringilla lectus a mauris iaculis, eu bibendum nulla vulputate. Duis rutrum metus nec ligula vulputate, vitae efficitur donec faucibus.</p><div class="product-price"><span class="old">$111.11</span><span class="now">$99.99</span></div></article>
  <article class="product" style="left:408px;top:790px"><div class="product-photo" role="img" aria-label="Smartphone product photo"></div><h3 class="product-name">LOREM IPSUM</h3><p class="product-desc">Lorem ipsum dolor sit amet, consectetur adipiscing elit. Nulla congue risus ut nisl placerat, sed rutrum lacus dignissim. Donec fringilla lectus a mauris iaculis, eu bibendum nulla vulputate. Duis rutrum metus nec ligula vulputate, vitae efficitur donec faucibus.</p><div class="product-price"><span class="old">$111.11</span><span class="now">$99.99</span></div></article>
  <article class="product" style="left:608px;top:790px"><div class="product-photo" role="img" aria-label="Smartphone product photo"></div><h3 class="product-name">LOREM IPSUM</h3><p class="product-desc">Lorem ipsum dolor sit amet, consectetur adipiscing elit. Nulla congue risus ut nisl placerat, sed rutrum lacus dignissim. Donec fringilla lectus a mauris iaculis, eu bibendum nulla vulputate. Duis rutrum metus nec ligula vulputate, vitae efficitur donec faucibus.</p><div class="product-price"><span class="old">$111.11</span><span class="now">$99.99</span></div></article>
  <article class="product" style="left:808px;top:790px"><div class="product-photo" role="img" aria-label="Smartphone product photo"></div><h3 class="product-name">LOREM IPSUM</h3><p class="product-desc">Lorem ipsum dolor sit amet, consectetur adipiscing elit. Nulla congue risus ut nisl placerat, sed rutrum lacus dignissim. Donec fringilla lectus a mauris iaculis, eu bibendum nulla vulputate. Duis rutrum metus nec ligula vulputate, vitae efficitur donec faucibus.</p><div class="product-price"><span class="old">$111.11</span><span class="now">$99.99</span></div></article>

  <!-- Row 2 -->
  <article class="product" style="left:208px;top:1123px"><div class="product-photo" role="img" aria-label="Smartphone product photo"></div><h3 class="product-name">LOREM IPSUM</h3><p class="product-desc">Lorem ipsum dolor sit amet, consectetur adipiscing elit. Nulla congue risus ut nisl placerat, sed rutrum lacus dignissim. Donec fringilla lectus a mauris iaculis, eu bibendum nulla vulputate. Duis rutrum metus nec ligula vulputate, vitae efficitur donec faucibus.</p><div class="product-price"><span class="old">$111.11</span><span class="now">$99.99</span></div></article>
  <article class="product" style="left:408px;top:1123px"><div class="product-photo" role="img" aria-label="Smartphone product photo"></div><h3 class="product-name">LOREM IPSUM</h3><p class="product-desc">Lorem ipsum dolor sit amet, consectetur adipiscing elit. Nulla congue risus ut nisl placerat, sed rutrum lacus dignissim. Donec fringilla lectus a mauris iaculis, eu bibendum nulla vulputate. Duis rutrum metus nec ligula vulputate, vitae efficitur donec faucibus.</p><div class="product-price"><span class="old">$111.11</span><span class="now">$99.99</span></div></article>
  <article class="product" style="left:608px;top:1123px"><div class="product-photo" role="img" aria-label="Smartphone product photo"></div><h3 class="product-name">LOREM IPSUM</h3><p class="product-desc">Lorem ipsum dolor sit amet, consectetur adipiscing elit. Nulla congue risus ut nisl placerat, sed rutrum lacus dignissim. Donec fringilla lectus a mauris iaculis, eu bibendum nulla vulputate. Duis rutrum metus nec ligula vulputate, vitae efficitur donec faucibus.</p><div class="product-price"><span class="old">$111.11</span><span class="now">$99.99</span></div></article>
  <article class="product" style="left:808px;top:1123px"><div class="product-photo" role="img" aria-label="Smartphone product photo"></div><h3 class="product-name">LOREM IPSUM</h3><p class="product-desc">Lorem ipsum dolor sit amet, consectetur adipiscing elit. Nulla congue risus ut nisl placerat, sed rutrum lacus dignissim. Donec fringilla lectus a mauris iaculis, eu bibendum nulla vulputate. Duis rutrum metus nec ligula vulputate, vitae efficitur donec faucibus.</p><div class="product-price"><span class="old">$111.11</span><span class="now">$99.99</span></div></article>

  <!-- Row 3 -->
  <article class="product" style="left:208px;top:1456px"><div class="product-photo" role="img" aria-label="Smartphone product photo"></div><h3 class="product-name">LOREM IPSUM</h3><p class="product-desc">Lorem ipsum dolor sit amet, consectetur adipiscing elit. Nulla congue risus ut nisl placerat, sed rutrum lacus dignissim. Donec fringilla lectus a mauris iaculis, eu bibendum nulla vulputate. Duis rutrum metus nec ligula vulputate, vitae efficitur donec faucibus.</p><div class="product-price"><span class="old">$111.11</span><span class="now">$99.99</span></div></article>
  <article class="product" style="left:408px;top:1456px"><div class="product-photo" role="img" aria-label="Smartphone product photo"></div><h3 class="product-name">LOREM IPSUM</h3><p class="product-desc">Lorem ipsum dolor sit amet, consectetur adipiscing elit. Nulla congue risus ut nisl placerat, sed rutrum lacus dignissim. Donec fringilla lectus a mauris iaculis, eu bibendum nulla vulputate. Duis rutrum metus nec ligula vulputate, vitae efficitur donec faucibus.</p><div class="product-price"><span class="old">$111.11</span><span class="now">$99.99</span></div></article>
  <article class="product" style="left:608px;top:1456px"><div class="product-photo" role="img" aria-label="Smartphone product photo"></div><h3 class="product-name">LOREM IPSUM</h3><p class="product-desc">Lorem ipsum dolor sit amet, consectetur adipiscing elit. Nulla congue risus ut nisl placerat, sed rutrum lacus dignissim. Donec fringilla lectus a mauris iaculis, eu bibendum nulla vulputate. Duis rutrum metus nec ligula vulputate, vitae efficitur donec faucibus.</p><div class="product-price"><span class="old">$111.11</span><span class="now">$99.99</span></div></article>
  <article class="product" style="left:808px;top:1456px"><div class="product-photo" role="img" aria-label="Smartphone product photo"></div><h3 class="product-name">LOREM IPSUM</h3><p class="product-desc">Lorem ipsum dolor sit amet, consectetur adipiscing elit. Nulla congue risus ut nisl placerat, sed rutrum lacus dignissim. Donec fringilla lectus a mauris iaculis, eu bibendum nulla vulputate. Duis rutrum metus nec ligula vulputate, vitae efficitur donec faucibus.</p><div class="product-price"><span class="old">$111.11</span><span class="now">$99.99</span></div></article>

  <a class="see-more">SEE MORE <i>&gt;&gt;</i></a>

  <section class="promo" style="left:208px">
    <div class="promo-photo" role="img" aria-label="Photo of hands using smartphones"></div>
    <h3 class="promo-title">SUMMER SALE</h3>
    <p class="promo-text">Lorem ipsum dolor sit amet, consectetur adipiscing elit. Nulla congue risus ut nisl placerat, sed rutrum lacus dignissim. Donec fringilla lectus a mauris iaculis, eu bibendum nulla vulputate.</p>
  </section>
  <section class="promo" style="left:475px">
    <div class="promo-photo" role="img" aria-label="Photo of hands using smartphones"></div>
    <h3 class="promo-title">SUMMER SALE</h3>
    <p class="promo-text">Lorem ipsum dolor sit amet, consectetur adipiscing elit. Nulla congue risus ut nisl placerat, sed rutrum lacus dignissim. Donec fringilla lectus a mauris iaculis, eu bibendum nulla vulputate.</p>
  </section>
  <section class="promo" style="left:742px">
    <div class="promo-photo" role="img" aria-label="Photo of hands using smartphones"></div>
    <h3 class="promo-title">SUMMER SALE</h3>
    <p class="promo-text">Lorem ipsum dolor sit amet, consectetur adipiscing elit. Nulla congue risus ut nisl placerat, sed rutrum lacus dignissim. Donec fringilla lectus a mauris iaculis, eu bibendum nulla vulputate.</p>
  </section>
</main>

<footer class="site-footer">
  <span class="h" style="left:167px;top:51px">PRODUCTS</span>
  <span class="f" style="left:167px;top:90px">CELL PHONES</span>
  <span class="f" style="left:167px;top:124px">COMPUTERS</span>
  <span class="f" style="left:167px;top:158px">COMPUTERS</span>
  <span class="f" style="left:167px;top:192px">TV/VIDEO</span>

  <span class="f" style="left:333px;top:55px">AUDIO</span>
  <span class="f" style="left:333px;top:90px">CAMERAS</span>
  <span class="f" style="left:333px;top:124px">CAR</span>
  <span class="f" style="left:333px;top:158px">OFFICE</span>
  <span class="f" style="left:333px;top:192px">MUSIC</span>

  <span class="f" style="left:500px;top:55px">OTHERS</span>
  <span class="h" style="left:500px;top:84px">ABOUT US</span>
  <span class="h" style="left:500px;top:118px">NEWS</span>
  <span class="h" style="left:500px;top:152px">SERVICES</span>
  <span class="h" style="left:500px;top:186px">TODAY DEALS</span>

  <span class="h" style="left:667px;top:51px">HELP</span>
  <span class="h" style="left:667px;top:84px">SIGN IN</span>

  <div class="footer-divider"></div>

  <span class="h" style="left:904px;top:51px">CONTACT US</span>
  <span class="f" style="left:904px;top:90px">HELLO@CIRCUITCOVE.EXAMPLE</span>
  <span class="f" style="left:904px;top:124px">000-00000</span>
  <div class="social-dot" style="left:904px;top:151px"></div>
  <span class="f" style="left:940px;top:157px">FOLLOW US</span>
  <div class="social-dot" style="left:904px;top:183px"></div>
  <span class="f" style="left:940px;top:189px">LIKE US</span>
</footer>

<div class="base-bar">Copyright Info &nbsp;|&nbsp; Phone Number &nbsp;|&nbsp; Privacy Policy and Terms of Use</div>

</body>
</html>
```